Single Landing Page Redesign - CRO Experts Welcome!

We need our landing page redesigned. We will be giving a lot of weight to conversion optimization so be sure to redesign the landing page with conversion optimization concepts in mind.

This is the landing page that needs to be redesigned:
http://www.pagecrateworks.example/message_board/forum3.html

Here are some ideas that we think could increase conversions in order of priority:

- Show a screenshot of an example forum, linked to the forum's address (http://forums.mindlantern.example/)

- Change the "Get Feedback from Users" feature to "Mobile Friendly (perhaps a picture of an iphone with a mobile version of our forum loaded in it? - mobile version isn't launched yet)

- Mention "Social Sharing" as a feature. (perhaps mention something about content going viral?)

- Additional testimonials:
"Pagecrate Works has been a superb solution for GoldenVow Journeys. Our customers love it-and the customization available is flexible enough to allow us to "brand" the forums so that they fit with our main site. Tech support has been outstanding, with quick & helpful responses to the questions we've had."
Daniel Ferrow
www.goldenvow.example

"Very simple and easy to set up, yet so customizable. It looks like it resides right on our site."
Tobias Wendling
www.pvtrsa.example

- Additional client logo: swiftrail coaches (swiftrail.example) - It would be better if logos are in a horizontal line in gray.

- Benefits of creating a forum (paragraph or bullet points or any other creative way): Running a forum is an excellent way of creating a community. It can be a place for people to discuss issues, share knowledge, and talk about you, your product, or your service. In the long-term, providing a way for your users to be part of a community can prove to be invaluable in terms of search engine optimization, customer satisfaction, customer/visitor retention, brand awareness, customer support, viral promotion, building trust, and creating a new revenue stream.

- Additional info that can be included, which might increase conversions (not mandatory) (can be reworded or changed as needed):
Embed your forum into an existing website in seconds!
Cloud-Based
Secure - Our forums are equipped with security features that make hackers and spammers a thing of the past.

You are welcome to implement your own ideas as well.

Nice landing pages:
http://www.trymeadowly.example/ (I love the big, wide design.)
http://www.quarnix.example/crm/

The physical layout of the page can be changed completely. The existing text and elements of the landing page can be changed completely. None of the existing landing page has to remain the way it is. Be creative and come up with what you think looks best. The existing landing page is only an example of what we currently have.

The PSD of our logo is attached.

We look forward to seeing your mockups!

```html
<!DOCTYPE html>
<html lang="en">
<head>
<meta charset="utf-8">
<title>Pagecrate Works – Create a Powerful Forum</title>
<link href="https://fonts.googleapis.com/css2?family=Mulish:wght@400;600;700&display=swap" rel="stylesheet">
<style>
:root{
  --ink:#333a40;
  --muted:#6b7075;
  --accent:#4d7ea8;
  --link:#5a86b0;
  --navy:#1d3f5f;
  --band:#587593;
  --cyan:#2aa4d6;
  --panel:#f1f1f1;
  --line:#d9dcdf;
  --icon:#8fa3b8;
  --white:#ffffff;
}
*{box-sizing:border-box;margin:0;padding:0}
html,body{width:1200px;height:2341px;overflow:hidden}
body{font-family:"Mulish",Arial,sans-serif;color:var(--ink);background:var(--white);position:relative}
section,header,footer{position:absolute;left:0;width:1200px}
.abs{position:absolute}

/* header */
.site-header{top:0;height:75px;border-bottom:1px solid #e6e6e6;background:var(--white)}
.brand{left:289px;top:25px;display:flex;align-items:center;gap:7px;font-weight:700;font-size:13px;color:#375a7f;white-space:nowrap}
.brand-dot{width:24px;height:24px;border-radius:50%;border:3px solid #6f8fae}
.main-nav{left:448px;top:31px;font-size:11px;color:var(--link);display:flex;gap:12px;white-space:nowrap}
.main-nav span.sep{color:#aab7c4}
.talk{left:727px;top:26px;display:flex;align-items:center;gap:8px;white-space:nowrap}
.talk-label{font-size:12px;color:var(--cyan)}
.talk-number{font-size:17px;color:var(--ink);font-weight:600}

/* hero */
.hero{top:75px;height:281px;background:linear-gradient(#fafafa,#fff)}
.hero-title{left:291px;top:20px;font-size:27px;color:var(--accent);font-weight:400}
.hero-sub{left:291px;top:52px;font-size:21px;color:var(--ink)}
.hero-offer{left:292px;top:177px;z-index:4;white-space:nowrap}
.hero-offer h2{font-size:16px;font-weight:400;color:#2d4e6e;display:flex;align-items:center;gap:7px;letter-spacing:-.2px}
.hero-offer p{font-size:11px;color:var(--link);margin-left:20px}
.slide-arrow{top:162px;width:28px;height:28px;border:1px solid #e2e2e2;background:#fff;display:flex;align-items:center;justify-content:center}
.laptop{left:546px;top:85px;z-index:3}

/* band */
.cta-band{top:356px;height:120px;background:var(--band)}
.cta-band p{left:289px;top:40px;width:420px;font-size:17px;color:var(--white);line-height:1.35}
.btn{background:var(--navy);color:var(--white);font-size:12px;letter-spacing:.3px;display:flex;align-items:center;justify-content:center;white-space:nowrap}
.cta-band .btn{left:741px;top:62px;width:164px;height:36px}

/* quick features */
.quick{top:476px;height:286px;background:var(--panel)}
.quick-item{width:290px;padding-bottom:10px;border-bottom:1px solid var(--line)}
.quick-item.last{border-bottom:none}
.quick-item h3{font-size:13px;font-weight:400;color:var(--ink);display:flex;align-items:center;gap:8px}
.quick-item p{font-size:9.5px;color:var(--muted);margin-left:24px;line-height:1.4}

/* testimonial */
.testimonial{top:762px;height:174px;background:var(--white)}
.quote{left:289px;top:22px;width:620px;font-size:17px;color:var(--link);line-height:1.3;padding-left:24px}
.quote .mark{color:#b8c3cd;font-size:30px;font-weight:700;line-height:0}
.badge{left:313px;top:88px}
.rank{left:376px;top:108px;font-size:10px;color:var(--ink);line-height:1.4}
.dots{left:860px;top:102px;display:flex;gap:4px}
.dots i{width:8px;height:8px;border-radius:50%;background:#b8c3cd}
.dots i.on{background:#6f8fae}

/* feature icons */
.features{top:936px;height:590px;background:#f3f3f3}
.section-title{font-size:19px;color:var(--navy);font-weight:600}
.features .section-title{left:296px;top:24px}
.feature{width:205px;text-align:center}
.feature svg{display:block;margin:0 auto 12px}
.feature h3{font-size:12px;font-weight:400;color:var(--icon);margin-bottom:3px}
.feature p{font-size:9.5px;color:var(--ink);line-height:1.35}
.vline{width:1px;background:#dedede}

/* clients */
.clients{top:1526px;height:133px;background:var(--white)}
.clients .section-title{left:296px;top:22px}
.client-row{left:296px;top:68px;width:612px;display:flex;justify-content:space-between;align-items:center}
.client{font-size:14px;font-weight:700;color:#7a7f84;display:flex;align-items:center;gap:6px}
.client i{width:18px;height:18px;background:#9a9fa4;display:inline-block}
.client i.round{border-radius:50%}

/* benefits */
.benefits{top:1659px;height:242px;background:var(--panel)}
.benefits .section-title{left:296px;top:20px}
.benefit-list{left:296px;top:58px;width:620px;list-style:none}
.benefit-list li{font-size:12px;color:var(--accent);line-height:1.35;padding-left:20px;position:relative;margin-bottom:8px}
.benefit-list li::before{content:"✸";position:absolute;left:0;top:0;color:#8fa3b8}
.benefits .btn{left:315px;top:180px;width:164px;height:35px}

/* video */
.video{top:1901px;height:252px;background:var(--white)}
.monitor{left:300px;top:26px}
.video h2{left:587px;top:44px;font-size:18px;font-weight:400;color:var(--navy)}
.video-copy{left:590px;top:112px;width:290px;font-size:12px;color:var(--link);line-height:1.35}
.video-copy p{margin-bottom:12px}

/* newsletter */
.newsletter{top:2153px;height:128px;background:var(--band);color:var(--white)}
.newsletter h2{left:303px;top:16px;font-size:17px;font-weight:400}
.newsletter .intro{left:303px;top:42px;width:270px;font-size:8.5px;line-height:1.35}
.signup{left:303px;top:78px;display:flex;gap:6px}
.signup .field{width:252px;height:22px;background:#fff;color:#888;font-size:9px;padding:5px 7px}
.signup .btn{width:70px;height:22px;font-size:9px}
.call{left:758px;top:22px;font-size:11px}
.call-number{left:745px;top:38px;font-size:19px;font-weight:600;display:flex;align-items:center;gap:4px}
.follow{left:758px;top:72px;font-size:11px;display:flex;gap:6px;align-items:center}
.follow span.net{font-size:9px;border:1px solid #fff;border-radius:10px;padding:2px 6px}

.site-footer{top:2281px;height:60px;background:var(--white)}
.site-footer p{position:absolute;left:303px;top:26px;font-size:8px;color:#999}
</style>
</head>
<body>

<header class="site-header">
  <div class="abs brand"><span class="brand-dot"></span>Pagecrate Works</div>
  <nav class="abs main-nav"><span>Home</span><span class="sep">|</span><span>Features</span><span class="sep">|</span><span>Pricing</span><span class="sep">|</span><span>Contact Us</span></nav>
  <div class="abs talk"><span class="talk-label">Want to Talk?</span><span class="talk-number">1-800-555-0142</span></div>
</header>

<section class="hero">
  <h1 class="abs hero-title">The Easiest Way to Create a Powerful Forum</h1>
  <p class="abs hero-sub">No Coding, Software, or Servers!</p>
  <div class="abs slide-arrow" style="left:236px"><svg width="10" height="14"><path d="M8 1 2 7l6 6" stroke="#666" fill="none" stroke-width="1.5"/></svg></div>
  <div class="abs slide-arrow" style="left:936px"><svg width="10" height="14"><path d="M2 1l6 6-6 6" stroke="#666" fill="none" stroke-width="1.5"/></svg></div>
  <div class="abs hero-offer">
    <h2><span style="color:#6f8fae;font-size:13px">✸</span>Try Any Plan Free For One Week.</h2>
    <p>No Credit Card Required. No Commitment.</p>
  </div>
  <svg class="abs laptop" width="406" height="230" viewBox="0 0 406 230" aria-label="Example MindLantern forum">
    <rect x="38" y="0" width="330" height="218" rx="8" fill="#111"/>
    <rect x="48" y="10" width="310" height="200" fill="#fff"/>
    <text x="56" y="22" font-size="5" fill="#2d4e6e" font-weight="700">MindLantern</text>
    <text x="56" y="42" font-size="6" fill="#333" font-weight="700">MindLantern Forum</text>
    <rect x="180" y="50" width="170" height="8" fill="#e6eef6"/>
    <text x="190" y="56" font-size="4" fill="#333">Register    Login    Search    New Posts</text>
    <rect x="56" y="62" width="294" height="8" fill="#f2f2f2"/>
    <text x="60" y="68" font-size="4" fill="#555">Forums</text>
    <rect x="56" y="84" width="294" height="6" fill="#dbe6f0"/>
    <text x="60" y="89" font-size="4" fill="#333">Forum                                                              Posts  Topics  Last Post</text>
    <rect x="56" y="91" width="294" height="6" fill="#6f9cc8"/>
    <text x="60" y="96" font-size="4" fill="#fff">General Discussion</text>
    <g font-size="3.6" fill="#4d7ea8">
      <text x="64" y="105">Updates and Releases</text><text x="64" y="121">News and Events</text><text x="64" y="137">Product Support</text>
      <text x="240" y="105">Latest update shared</text><text x="240" y="121">Meetup this month</text><text x="240" y="137">Setup question answered</text>
    </g>
    <g stroke="#e2e2e2"><line x1="56" y1="113" x2="350" y2="113"/><line x1="56" y1="129" x2="350" y2="129"/><line x1="56" y1="145" x2="350" y2="145"/></g>
    <rect x="56" y="147" width="294" height="6" fill="#6f9cc8"/>
    <text x="60" y="152" font-size="4" fill="#fff">Tips and Tricks</text>
    <text x="64" y="162" font-size="3.6" fill="#4d7ea8">Share Your Workflow</text>
    <path d="M0 218h406v6q0 6-8 6H8q-8 0-8-6z" fill="#c9ccd0"/>
    <rect x="170" y="218" width="66" height="4" rx="2" fill="#9ea3a8"/>
  </svg>
</section>

<section class="cta-band">
  <p class="abs">Pagecrate Works proudly serves over 100 million visits per month to over 15,000 forums...</p>
  <div class="abs btn">CREATE A FORUM NOW</div>
</section>

<section class="quick">
  <div class="abs quick-item" style="left:289px;top:30px"><h3><svg width="16" height="16"><circle cx="8" cy="9" r="6" fill="none" stroke="#888" stroke-width="1.5"/><path d="M8 9V5M6 2h4" stroke="#888" stroke-width="1.5"/></svg>Instant Setup</h3><p>So easy to use, you'll be up and running in a few seconds!</p></div>
  <div class="abs quick-item" style="left:289px;top:92px"><h3><svg width="16" height="16"><rect x="2" y="4" width="12" height="9" fill="none" stroke="#888" stroke-width="1.5"/></svg>Public or Private</h3><p>You can let the whole world view and contribute to your forum, or limit access to a select few.</p></div>
  <div class="abs quick-item" style="left:289px;top:156px"><h3><svg width="16" height="16"><path d="M3 15V2h9l-2 3 2 3H3" fill="#888"/></svg>White Label</h3><p>Use your own logo and domain name. Pagecrate Works is completely invisible to your users!</p></div>
  <div class="abs quick-item last" style="left:289px;top:222px"><h3><svg width="16" height="16"><circle cx="6.5" cy="6.5" r="4.5" fill="none" stroke="#888" stroke-width="2"/><path d="M10 10l5 5" stroke="#888" stroke-width="2"/></svg>SEO Friendly</h3><p>Search Engine Optimization is built into the foundation, driving more traffic to your forum.</p></div>
  <div class="abs quick-item" style="left:600px;top:30px"><h3><svg width="16" height="16"><path d="M2 14 8 2l6 12M4 10h8" fill="none" stroke="#888" stroke-width="1.5"/></svg>Fully Customizable</h3><p>Customize every aspect of your forum, including the design and features.</p></div>
  <div class="abs quick-item" style="left:600px;top:92px"><h3><svg width="16" height="16"><ellipse cx="8" cy="9" rx="6" ry="5" fill="#888"/></svg>Monetization</h3><p>Make money from your forum by adding your own advertising.</p></div>
  <div class="abs quick-item" style="left:600px;top:156px"><h3><svg width="16" height="16"><circle cx="8" cy="8" r="6" fill="none" stroke="#888" stroke-width="2"/><circle cx="8" cy="8" r="2.5" fill="none" stroke="#888" stroke-width="1.5"/></svg>Fanatic Support</h3><p>Industry-leading phone, chat, and email support.</p></div>
  <div class="abs quick-item last" style="left:600px;top:222px"><h3><svg width="16" height="16"><rect x="2" y="3" width="12" height="9" fill="none" stroke="#888" stroke-width="1.5"/><path d="M5 6h6M5 9h4" stroke="#888"/></svg>Moderation</h3><p>You decide who can view and post content. Review and approve content before it goes live.</p></div>
</section>

<section class="testimonial">
  <p class="abs quote"><span class="mark" style="position:absolute;left:0;top:14px">"</span>Excellent customer service... amazing features... Pagecrate Works proved to be one of the most comprehensive forum services we came across... It doesn't get more user-friendly than this... <span class="mark">"</span></p>
  <svg class="abs badge" width="46" height="56" role="img" aria-label="Ranking award badge"><circle cx="23" cy="22" r="20" fill="#c63a2f"/><path d="M12 38l-4 16 15-8 15 8-4-16z" fill="#a82c23"/></svg>
  <p class="abs rank">Ranked #1 by RateHarbor<br>www.rateharbor.example</p>
  <div class="abs dots"><i class="on"></i><i></i><i></i><i></i></div>
</section>

<section class="features">
  <h2 class="abs section-title">The Features You Need With The Ease You Expect...</h2>
  <div class="abs vline" style="left:490px;top:80px;height:450px"></div>
  <div class="abs vline" style="left:700px;top:80px;height:300px"></div>

  <div class="abs feature" style="left:285px;top:72px">
    <svg width="72" height="72"><circle cx="36" cy="36" r="34" fill="#8fa3b8"/><text x="36" y="41" font-size="11" fill="#fff" text-anchor="middle" font-family="Mulish,sans-serif" font-weight="700">Friendnet</text></svg>
    <h3>Login with Friendnet</h3><p>Users can login to your forum with their Friendnet account, increasing participation by an average of 50%!</p></div>
  <div class="abs feature" style="left:492px;top:72px">
    <svg width="72" height="72"><rect x="27" y="4" width="18" height="38" rx="9" fill="#8fa3b8"/><path d="M20 32q0 18 16 18t16-18" fill="none" stroke="#8fa3b8" stroke-width="4"/><path d="M36 50v16M26 68h20" stroke="#8fa3b8" stroke-width="4"/></svg>
    <h3>Use Friendnet-Style Chat</h3><p>Users can chat and instant message each other with a built-in chat room and friendnet-style chat bar.</p></div>
  <div class="abs feature" style="left:705px;top:72px">
    <svg width="72" height="72"><path d="M2 10h24l6 6h38v52H2z" fill="#8fa3b8"/><rect x="8" y="22" width="60" height="42" fill="#fff" opacity=".35"/><rect x="28" y="32" width="28" height="22" fill="#fff"/><path d="M30 52l8-10 6 6 4-4 6 8z" fill="#8fa3b8"/></svg>
    <h3>Share Files, Photos, and Videos</h3><p>Users can attach files and photos to posts, embed videos, or upload their own profile picture and avatar image.</p></div>

  <div class="abs feature" style="left:285px;top:250px">
    <svg width="72" height="72"><circle cx="36" cy="36" r="32" fill="none" stroke="#8fa3b8" stroke-width="5"/><rect x="20" y="20" width="32" height="30" fill="none" stroke="#8fa3b8" stroke-width="3"/><text x="36" y="45" font-size="16" fill="#8fa3b8" text-anchor="middle" font-family="Mulish,sans-serif" font-weight="700">19</text></svg>
    <h3>Announce and Organize Events</h3><p>The built-in calendar makes managing events easier than ever.</p></div>
  <div class="abs feature" style="left:492px;top:250px">
    <svg width="72" height="72"><rect x="22" y="2" width="28" height="68" rx="6" fill="#8fa3b8"/><rect x="26" y="12" width="20" height="46" fill="#fff"/><circle cx="36" cy="64" r="3" fill="#fff"/></svg>
    <h3>Mobile Friendly</h3><p>Lorem ipsum dolor sit amet, consectetuer adipiscing elit, sed diam nonummy nibh euismod tincidunt ut laoreet dolore.</p></div>
  <div class="abs feature" style="left:705px;top:250px">
    <svg width="72" height="72"><path d="M10 62 48 24" stroke="#8fa3b8" stroke-width="8" stroke-linecap="round"/><circle cx="54" cy="16" r="12" fill="#8fa3b8"/><circle cx="58" cy="12" r="5" fill="#f3f3f3"/><path d="M14 10l48 48" stroke="#8fa3b8" stroke-width="6" stroke-linecap="round"/><rect x="6" y="4" width="14" height="10" fill="#8fa3b8" transform="rotate(45 13 9)"/></svg>
    <h3>Set User Permissions</h3><p>Control exactly who can access what, with incredible precision. Easily approve posts and registrations, privatize your forum, and much more.</p></div>

  <div class="abs feature" style="left:492px;top:418px">
    <svg width="72" height="72"><circle cx="36" cy="36" r="30" fill="#8fa3b8"/><text x="36" y="41" font-size="13" fill="#fff" text-anchor="middle" font-family="Mulish,sans-serif" font-weight="700">Share</text></svg>
    <h3>Social Sharing</h3><p>Lorem ipsum dolor sit amet, consectetuer adipiscing elit, sed diam nonummy nibh euismod tincidunt ut laoreet dolore.</p></div>
</section>

<section class="clients">
  <h2 class="abs section-title">Featured Clients</h2>
  <div class="abs client-row">
    <span class="client">Norvale</span>
    <span class="client"><i class="round"></i>Ashbury University</span>
    <span class="client">Frostel</span>
    <span class="client"><i></i>Civic Relief Aid</span>
    <span class="client">swiftrail coaches</span>
  </div>
</section>

<section class="benefits">
  <h2 class="abs section-title">Benefits Of Creating A Forum</h2>
  <ul class="abs benefit-list">
    <li>Running a forum is an excellent way of creating a community.</li>
    <li>It can be a place for people to discuss issues, share knowledge, and talk about you, your product, or your service.</li>
    <li>In the long-term, providing a way for your users to be part of a community can prove to be invaluable in terms of search engine optimization, customer satisfaction, customer/visitor retention, brand awareness, customer support, viral promotion, building trust, and creating a new revenue stream.</li>
  </ul>
  <div class="abs btn">CREATE A FORUM NOW</div>
</section>

<section class="video">
  <svg class="abs monitor" width="252" height="206">
    <defs><radialGradient id="vid"><stop offset="0" stop-color="#fbe6f3"/><stop offset="1" stop-color="#e58cc4"/></radialGradient></defs>
    <rect x="0" y="0" width="252" height="168" rx="6" fill="#1a1a1a"/>
    <rect x="8" y="8" width="236" height="144" fill="url(#vid)" role="img" aria-label="Introduction video preview with animated presenter"/>
    <circle cx="126" cy="80" r="14" fill="#4d7ea8" opacity=".85"/><path d="M121 72l12 8-12 8z" fill="#fff"/>
    <rect x="0" y="158" width="252" height="10" fill="#d9dadc"/>
    <path d="M104 168h44l6 28h-56z" fill="#c4c6c9"/><rect x="84" y="196" width="84" height="6" rx="3" fill="#b3b6b9"/>
  </svg>
  <svg class="abs" style="left:440px;top:58px" width="240" height="60"><path d="M2 56q90 6 150-10t78-44" fill="none" stroke="#2d4e6e" stroke-dasharray="2 3"/></svg>
  <h2 class="abs">Watch a 60 Second Introduction Video</h2>
  <div class="abs video-copy">
    <p>Embed your forum into an existing website in seconds! Cloud-Based</p>
    <p>Secure - Our forums are equipped with security features that make hackers and spammers a thing of the past</p>
  </div>
</section>

<section class="newsletter">
  <h2 class="abs">Subscribe To Our Newsletter!</h2>
  <p class="abs intro">Subscribe to get monthly updates in your inbox. You will receive product updates, productivity tips and exclusive offers.</p>
  <div class="abs signup"><div class="field">Enter Your Email Address</div><div class="btn">Subscribe</div></div>
  <p class="abs call">Call Us Today</p>
  <p class="abs call-number"><svg width="16" height="16"><path d="M3 1l3 0 2 4-2 2q2 3 4 4l2-2 4 2v3q-1 2-3 2Q3 14 1 3q0-2 2-2z" fill="#fff"/></svg>1-800-555-0142</p>
  <div class="abs follow">Follow Us <span class="net">Friendnet</span><span class="net">Chirp</span><span class="net">Linkwork</span><span class="net">Feed</span></div>
</section>

<footer class="site-footer"><p>© Copyright 2013 Pagecrate Works. All rights reserved.</p></footer>

</body>
</html>
```